Redesign Local Plumber Website

redesign of existing plumbing website

Mobile Responsive
Professional
modern
easy enquiry
Map embed

Please see existing site for text and images. Please feel free to suggest improvements and any additional features
letmefixyourtaps.com.au

attached is logo and the Australian owned badge which we also want featuring

Target Market(s)

Plumbing & Gas Services

Industry/Entity Type

Plumbing

Font styles to use
Sans Serif

Requirements
Must have
• existing logo
Nice to have
• new design
Should not have
• same design

```html
<!DOCTYPE html>
<html lang="en">
<head>
<meta charset="utf-8">
<title>Let Me Fix Your Taps – Plumbing &amp; Gas Services</title>
<link href="https://fonts.googleapis.com/css2?family=Poppins:wght@400;500;600&family=Montserrat:wght@400;500;600&display=swap" rel="stylesheet">
<style>
:root{
  --navy:#15145c;
  --blue:#1b90d2;
  --sky:#eaf3fb;
  --ink:#2b2b33;
  --muted:#55555f;
  --white:#ffffff;
  --rust:#8e2b22;
}
*{box-sizing:border-box;margin:0;padding:0}
html,body{width:1200px;height:4549px;overflow:hidden;background:var(--white)}
body{font-family:"Montserrat",sans-serif;color:var(--ink);position:relative}
.abs{position:absolute}
h1,h2,h3,h4{font-family:"Poppins",sans-serif;font-weight:500}
.brand{font-family:"Poppins",sans-serif;font-weight:600;color:var(--navy);display:flex;align-items:center;gap:10px;letter-spacing:.5px}
.brand .dot{width:34px;height:34px;border-radius:50%;background:var(--blue);flex:none}
.btn{position:absolute;border-radius:20px;font-size:13px;display:flex;align-items:center;justify-content:center;color:var(--white);font-family:"Montserrat",sans-serif}
.btn.navy{background:var(--navy)}
.btn.blue{background:var(--blue)}
.photo{position:absolute}
.badge{position:absolute;border-radius:50%;border:4px solid var(--navy);background:#dfe7f4}
/* header */
.contact-chip{position:absolute;top:34px;display:flex;align-items:center;gap:10px;font-size:11px;color:var(--navy)}
.contact-chip .ic{width:30px;height:30px;border-radius:50%;background:var(--blue);display:flex;align-items:center;justify-content:center}
.contact-chip small{display:block;color:var(--blue);font-size:10px}
.nav{position:absolute;top:94px;left:0;width:1200px;height:42px;background:var(--navy)}
.nav a{position:absolute;top:0;height:42px;line-height:42px;color:var(--white);font-size:13px;text-decoration:none;transform:translateX(-50%)}
.nav .active{background:var(--blue);left:162px;width:120px;transform:none;text-align:center}
.nav .tools{position:absolute;left:953px;top:0;width:247px;height:42px;background:var(--blue)}
/* hero */
.hero{position:absolute;top:136px;left:0;width:1200px;height:535px;background:linear-gradient(90deg,#f4f7fa 0%,#dfe8f0 40%,#b7c4d2 70%,#8ea0b3 100%)}
.hero-title{position:absolute;left:166px;top:193px;font-size:30px;color:var(--blue)}
.hero-text{position:absolute;left:166px;top:236px;width:370px;font-size:13px;line-height:20px;color:var(--muted)}
.slider{position:absolute;left:42px;top:240px;font-size:12px;color:var(--muted);display:flex;align-items:center;gap:6px}
.slider .bar{width:4px;height:46px;background:linear-gradient(var(--navy) 0 40%,var(--blue) 40% 100%)}
/* sections */
.sec-title{position:absolute;font-size:30px;color:var(--ink)}
.body-text{position:absolute;font-size:12.5px;line-height:16px;color:var(--muted)}
.years{position:absolute;left:438px;top:1090px;width:127px;height:125px;background:var(--blue);color:var(--white);padding:18px 16px;font-family:"Poppins",sans-serif}
.years b{display:block;font-size:28px;font-weight:600;line-height:32px}
.years span{font-size:13px;letter-spacing:1px}
.tile{position:absolute;top:1337px;width:428px;height:363px}
.tile .label{position:absolute;left:0;bottom:0;width:100%;height:61px;display:flex;align-items:center;justify-content:center;color:var(--white);font-family:"Poppins",sans-serif;font-size:30px;font-weight:500}
.services-band{position:absolute;top:1797px;left:0;width:602px;height:512px;background:var(--sky)}
.check-list{position:absolute;left:162px;top:1915px;width:385px;list-style:none}
.check-list li{display:flex;gap:12px;font-size:12.5px;line-height:15px;color:var(--muted);margin-bottom:17px}
.check-list li svg{flex:none;margin-top:-1px}
.product{position:absolute;top:2927px;width:209px;height:270px;text-align:center}
.product .img{height:208px}
.product .name{margin-top:12px;font-size:13px;color:var(--muted)}
.product .price{font-size:12px;color:#c2271f;margin-top:3px}
.product.hover{background:var(--blue)}
.product.hover .name,.product.hover .price{color:var(--white)}
.product .actions{position:absolute;top:100px;left:0;width:100%;display:flex;justify-content:center;gap:8px}
.product .actions span{width:26px;height:26px;border-radius:50%;background:var(--white)}
.card{position:absolute;top:3326px;width:274px;height:240px;color:var(--white);text-align:center;padding:24px 18px}
.card h4{font-size:16px;margin:10px 0 8px}
.card p{font-size:11.5px;line-height:14px}
.card .cbtn{display:inline-block;margin-top:12px;padding:8px 44px;border-radius:18px;font-size:12px}
/* contact */
.contact-band{position:absolute;top:3667px;left:0;width:602px;height:437px;background:var(--blue)}
.field{position:absolute;background:var(--white);font-size:13px;color:var(--muted);padding:6px 12px}
.map{position:absolute;top:3667px;left:602px;width:598px;height:437px;background:linear-gradient(135deg,#eef0ec,#e2e6e0 50%,#d8dfe6)}
.map-card{position:absolute;left:688px;top:3842px;width:309px;height:142px;background:var(--white);box-shadow:0 2px 8px rgba(0,0,0,.18);padding:14px 20px;font-size:12px;line-height:22px;color:var(--ink)}
/* footer */
.footer{position:absolute;top:4104px;left:0;width:1200px;height:378px;background:var(--navy);color:var(--white)}
.partner{position:absolute;left:74px;width:223px;height:56px;background:var(--white);border:3px solid #c9202a;display:flex;align-items:center;justify-content:center;font-family:"Poppins",sans-serif;font-size:22px;font-weight:500;color:var(--navy)}
.foot-title{position:absolute;top:4186px;font-family:"Poppins",sans-serif;font-size:16px;color:var(--white)}
.foot-links{position:absolute;left:344px;top:4224px;list-style:none;font-size:12.5px;line-height:24px;color:var(--white)}
.foot-links li::before{content:"•";margin-right:10px}
.foot-info{position:absolute;left:505px;font-size:12px;display:flex;gap:12px;align-items:center;color:var(--white)}
.pay{position:absolute;top:4406px;height:22px;width:34px;border-radius:3px;font-size:7px;display:flex;align-items:center;justify-content:center;font-weight:600;background:#e9eef7;color:var(--navy)}
.about-card{position:absolute;left:805px;top:4081px;width:317px;height:401px;background:var(--sky);padding:40px 46px;color:var(--ink)}
.copyright{position:absolute;left:74px;top:4507px;font-size:12px;color:var(--muted)}
.social{position:absolute;top:4504px;width:22px;height:22px;border-radius:50%}
</style>
</head>
<body>

<header>
  <div class="brand abs" style="left:160px;top:26px;font-size:17px"><span class="dot"></span>LET ME FIX YOUR TAPS</div>
  <div class="contact-chip" style="left:508px">
    <span class="ic"><svg width="14" height="14" viewBox="0 0 24 24"><path fill="#fff" d="M6.6 10.8a15.1 15.1 0 0 0 6.6 6.6l2.2-2.2c.3-.3.7-.4 1-.2 1.1.4 2.3.6 3.6.6.6 0 1 .4 1 1V20c0 .6-.4 1-1 1A17 17 0 0 1 3 4c0-.6.4-1 1-1h3.5c.6 0 1 .4 1 1 0 1.3.2 2.5.6 3.6.1.3 0 .7-.2 1z"/></svg></span>
    <div><small>Call Us</small>0400 555 123</div>
  </div>
  <div class="contact-chip" style="left:646px">
    <span class="ic"><svg width="14" height="14" viewBox="0 0 24 24"><path fill="#fff" d="M6.6 10.8a15.1 15.1 0 0 0 6.6 6.6l2.2-2.2c.3-.3.7-.4 1-.2 1.1.4 2.3.6 3.6.6.6 0 1 .4 1 1V20c0 .6-.4 1-1 1A17 17 0 0 1 3 4c0-.6.4-1 1-1h3.5c.6 0 1 .4 1 1 0 1.3.2 2.5.6 3.6.1.3 0 .7-.2 1z"/></svg></span>
    <div><small>Email us</small>office@letmefixyourtaps.com.au</div>
  </div>
  <div class="btn blue" style="left:916px;top:37px;width:139px;height:34px">Get a Quote</div>
  <nav class="nav">
    <a class="active">Home</a>
    <a style="left:348px">About Us</a>
    <a style="left:482px">Services</a>
    <a style="left:607px">Septic</a>
    <a style="left:734px">Products</a>
    <a style="left:877px">Contact Us</a>
    <div class="tools">
      <svg class="abs" style="left:32px;top:15px" width="12" height="12" viewBox="0 0 24 24"><circle cx="10" cy="10" r="7" fill="none" stroke="#fff" stroke-width="3"/><path d="M15 15l7 7" stroke="#fff" stroke-width="3"/></svg>
      <svg class="abs" style="left:66px;top:14px" width="14" height="14" viewBox="0 0 24 24"><path d="M2 3h4l3 12h11l2-8H7" fill="none" stroke="#fff" stroke-width="2.5"/><circle cx="10" cy="20" r="2" fill="#fff"/><circle cx="18" cy="20" r="2" fill="#fff"/></svg>
    </div>
  </nav>
</header>

<section class="hero">
  <div class="photo" role="img" aria-label="Plumber repairing pipes under a kitchen sink" style="left:470px;top:0;width:730px;height:535px;background:linear-gradient(90deg,rgba(255,255,255,0),rgba(60,85,120,.35) 60%,rgba(40,60,95,.5))"></div>
  <div class="slider"><span class="bar"></span>— 02</div>
  <h1 class="hero-title">Plumbing &amp; Gas Services</h1>
  <p class="hero-text">Lorem Ipsum is simply dummy ever text printing and typesetting a ever since the 1500s</p>
  <div class="btn navy" style="left:164px;top:305px;width:136px;height:32px">Read More</div>
  <div class="btn blue" style="left:314px;top:305px;width:136px;height:32px">Get a Quote</div>
</section>

<section>
  <h2 class="sec-title" style="left:0;width:1200px;text-align:center;top:736px">About us</h2>
  <div class="photo" role="img" aria-label="Company mascot illustration" style="left:60px;top:880px;width:226px;height:372px;background:radial-gradient(ellipse at center,#d7dbef 0%,#eef0f8 70%,rgba(255,255,255,0) 72%)"></div>
  <div class="photo" role="img" aria-label="Plumbing fittings, pipe wrench and tape on a workbench" style="left:173px;top:823px;width:348px;height:263px;background:linear-gradient(135deg,#3a3d44,#6d7078 50%,#9a4a3c)"></div>
  <div class="years"><b>30<br>YEARS</b><span>EXPERIENCE</span></div>
  <h3 class="abs" style="left:600px;top:812px;font-size:25px">Who we are</h3>
  <p class="body-text" style="left:602px;top:863px;width:445px">Daniel has been in the plumbing and gas industry since high school, his father Ray was a plumber and estimator. Daniel has trained with reputable plumbers of his time and achieved apprentice of the year 2 years running, then taking out the “Apprentice of the Year” award for all trades during his apprenticeship.</p>
  <p class="body-text" style="left:602px;top:959px;width:445px">A member of Trade Guild master-plumbing and an EcoTrade West Plumber. Daniel maintains a high level of education and frequently refreshes his knowledge with current trends and regulations.</p>
  <div class="btn navy" style="left:602px;top:1054px;width:136px;height:31px">Read More</div>
  <div class="badge" style="left:612px;top:1124px;width:92px;height:92px" aria-label="Trade association badge"></div>
  <div class="abs" style="left:741px;top:1122px;width:48px;height:97px;background:#dfe7f4;border:3px solid var(--navy);border-radius:24px 24px 4px 4px" aria-label="Specialist certification badge"></div>
  <div class="badge" style="left:838px;top:1124px;width:78px;height:78px;border-color:#3d9b3d;background:#e6f3e0" aria-label="Sustainability badge"></div>
</section>

<section>
  <div class="tile" style="left:162px">
    <div class="photo" role="img" aria-label="Hand tightening a tap with a wrench" style="left:0;top:0;width:428px;height:302px;background:linear-gradient(135deg,#c9ccd0,#8c9096 60%,#d8c7b4)"></div>
    <div class="label" style="background:var(--blue)">Plumbing</div>
  </div>
  <div class="tile" style="left:612px">
    <div class="photo" role="img" aria-label="Stainless steel gas cooktop burners" style="left:0;top:0;width:429px;height:302px;background:linear-gradient(135deg,#8b98aa,#3f4652 55%,#6f7b8c)"></div>
    <div class="label" style="background:var(--navy)">Gas</div>
  </div>
</section>

<section>
  <div class="services-band"></div>
  <div class="photo" role="img" aria-label="Plumber lying on a bathroom floor fixing pipes behind a toilet" style="left:602px;top:1797px;width:598px;height:512px;background:linear-gradient(135deg,#e9e6e1,#c8c2b8 45%,#2a3e78 70%,#c9b79d)"></div>
  <h2 class="sec-title" style="left:162px;top:1853px;font-size:30px">Services That We Offer</h2>
  <ul class="check-list" style="width:385px">
    <li><svg width="16" height="16" viewBox="0 0 24 24"><circle cx="12" cy="12" r="10" fill="none" stroke="#1b90d2" stroke-width="2.5"/><path d="M7 12l4 4 7-8" fill="none" stroke="#1b90d2" stroke-width="2.5"/></svg>All Plumbing and Gas installations</li>
    <li><svg width="16" height="16" viewBox="0 0 24 24"><circle cx="12" cy="12" r="10" fill="none" stroke="#1b90d2" stroke-width="2.5"/><path d="M7 12l4 4 7-8" fill="none" stroke="#1b90d2" stroke-width="2.5"/></svg>Renovations and New Housing</li>
    <li><svg width="16" height="16" viewBox="0 0 24 24"><circle cx="12" cy="12" r="10" fill="none" stroke="#1b90d2" stroke-width="2.5"/><path d="M7 12l4 4 7-8" fill="none" stroke="#1b90d2" stroke-width="2.5"/></svg>Repairs and maintenance</li>
    <li><svg width="16" height="16" viewBox="0 0 24 24"><circle cx="12" cy="12" r="10" fill="none" stroke="#1b90d2" stroke-width="2.5"/><path d="M7 12l4 4 7-8" fill="none" stroke="#1b90d2" stroke-width="2.5"/></svg>Supply and installation of Hot Water Units</li>
    <li><svg width="16" height="16" viewBox="0 0 24 24"><circle cx="12" cy="12" r="10" fill="none" stroke="#1b90d2" stroke-width="2.5"/><path d="M7 12l4 4 7-8" fill="none" stroke="#1b90d2" stroke-width="2.5"/></svg>Supply and install pumps, domestic pressure pumps and sewerage sump pumps</li>
    <li><svg width="16" height="16" viewBox="0 0 24 24"><circle cx="12" cy="12" r="10" fill="none" stroke="#1b90d2" stroke-width="2.5"/><path d="M7 12l4 4 7-8" fill="none" stroke="#1b90d2" stroke-width="2.5"/></svg>Approved Agent for Aqualine Waste Water Treatments Alternative Treatment Units</li>
    <li><svg width="16" height="16" viewBox="0 0 24 24"><circle cx="12" cy="12" r="10" fill="none" stroke="#1b90d2" stroke-width="2.5"/><path d="M7 12l4 4 7-8" fill="none" stroke="#1b90d2" stroke-width="2.5"/></svg>Supply and installation of tap ware and fixtures see products page Other than the general plumbing and gas installations, repairs and maintenance we also offer a great range of products we are agents for:</li>
  </ul>
</section>

<section>
  <div class="photo" role="img" aria-label="Garden sprinkler watering green grass" style="left:162px;top:2420px;width:428px;height:362px;background:linear-gradient(180deg,#e7f2d8,#9cc86a 45%,#3f7f22)"></div>
  <h2 class="abs" style="left:628px;top:2420px;font-size:29px;line-height:41px;color:var(--ink)">ATU’s<br>Alternative Treatment Units<br>(septic systems)</h2>
  <p class="body-text" style="left:628px;top:2568px;width:418px">Let Me Fix Your Taps is the authorised service agent in this area to supply and install the Aqualine range of ATU’s. Aqualine Wastewater Management is a local family company, the systems were developed and manufactured right here. Each unit is approved by the regional health authority, created for domestic house use and commercial applications. The internal system can be simply developed for use with business sites. A nutrient retentive system that leads to garden irrigation.</p>
  <div class="btn navy" style="left:630px;top:2750px;width:138px;height:32px">Read More</div>
</section>

<section>
  <h2 class="sec-title" style="left:0;width:1200px;text-align:center;top:2858px">Featured Products</h2>
  <div class="product" style="left:162px">
    <div class="img" role="img" aria-label="Stainless steel double kitchen sink" style="background:linear-gradient(160deg,#f1f1f1,#a9adb2)"></div>
    <div class="name">Product Name</div><div class="price">$00.00</div>
  </div>
  <div class="product" style="left:385px">
    <div class="img" role="img" aria-label="Red water pressure pump" style="background:radial-gradient(circle at 50% 55%,#d63a2b 0 30%,#f3f3f3 32%)"></div>
    <div class="name">Product Name</div><div class="price">$00.00</div>
  </div>
  <div class="product hover" style="left:607px">
    <div class="img" role="img" aria-label="Wall mounted basin" style="background:linear-gradient(180deg,#5ec4ea,#2da6d9)"></div>
    <div class="actions"><span></span><span></span><span></span></div>
    <div class="name">Product Name</div><div class="price">$00.00</div>
  </div>
  <div class="product" style="left:831px">
    <div class="img" role="img" aria-label="White close-coupled toilet" style="background:linear-gradient(160deg,#f4f4f4,#d2d2d2)"></div>
    <div class="name">Product Name</div><div class="price">$00.00</div>
  </div>
  <div class="btn navy" style="left:510px;top:3231px;width:194px;height:32px">View All Products</div>
</section>

<section>
  <div class="card" style="left:162px;background:var(--blue)">
    <svg width="40" height="44" viewBox="0 0 40 44"><circle cx="20" cy="25" r="16" fill="none" stroke="#fff" stroke-width="2.5"/><circle cx="20" cy="25" r="11" fill="none" stroke="#fff" stroke-width="1.5"/><path d="M20 25l-5-4M16 4h8M20 4v5" stroke="#fff" stroke-width="2.5" fill="none"/></svg>
    <h4>Quick Response</h4>
    <p>If you've had enough of tradespeople who never turn up when they say they will, call Daniel at Let Me Fix Your Taps.</p>
    <span class="cbtn" style="background:var(--navy)">Contact us</span>
  </div>
  <div class="card" style="left:464px;background:var(--navy)">
    <svg width="48" height="40" viewBox="0 0 48 40"><rect x="2" y="4" width="44" height="30" rx="3" fill="none" stroke="#fff" stroke-width="2.5"/><path d="M2 12h44M2 18h44" stroke="#fff" stroke-width="2.5"/><circle cx="36" cy="27" r="3" fill="none" stroke="#fff" stroke-width="2"/></svg>
    <h4>Payment Options</h4>
    <p>Electronic Transfer, Debit and Credit cards accepted, Debit Cards and EFTPOS facilities, Credit account to approved clients only. All accounts are COD unless by prior arrangement</p>
    <div style="display:flex;gap:4px;justify-content:center;margin-top:8px">
      <span style="width:36px;height:18px;background:#fff;border-radius:2px"></span><span style="width:36px;height:18px;background:#fff;border-radius:2px"></span><span style="width:36px;height:18px;background:#fff;border-radius:2px"></span><span style="width:36px;height:18px;background:#fff;border-radius:2px"></span>
    </div>
  </div>
  <div class="card" style="left:766px;background:linear-gradient(135deg,rgba(142,43,34,.92),rgba(110,30,30,.92))" role="img" aria-label="Showroom interior behind red overlay">
    <svg width="42" height="40" viewBox="0 0 42 40"><path d="M3 14l4-10h28l4 10M3 14h36v22H3z" fill="none" stroke="#fff" stroke-width="2.5"/><rect x="11" y="20" width="20" height="10" fill="none" stroke="#fff" stroke-width="2"/></svg>
    <h4>View our Showroom</h4>
    <p>We handle all plumbing and gas installation including domestic and commercial.</p>
    <span class="cbtn" style="background:var(--navy)">Visit our Showroom</span>
  </div>
</section>

<section>
  <div class="contact-band"></div>
  <h2 class="abs" style="left:162px;top:3728px;font-size:29px;color:var(--white)">Quick Contact</h2>
  <div class="field" style="left:162px;top:3784px;width:182px;height:32px">First Name</div>
  <div class="field" style="left:358px;top:3784px;width:180px;height:32px">Last Name</div>
  <div class="field" style="left:162px;top:3832px;width:182px;height:32px">Email</div>
  <div class="field" style="left:358px;top:3832px;width:180px;height:32px">Phone</div>
  <div class="field" style="left:162px;top:3880px;width:376px;height:111px">Message</div>
  <div class="btn navy" style="left:162px;top:4014px;width:154px;height:32px">Send</div>
  <div class="map" role="img" aria-label="Street map showing the business location"></div>
  <div class="map-card">
    <div class="brand" style="font-size:11px;gap:6px"><span class="dot" style="width:16px;height:16px"></span>LET ME FIX YOUR TAPS</div>
    Let Me Fix Your Taps, 27 Harlow Street<br>Brenmoor WA 6999<br>(08) 9000 0123 &nbsp;&nbsp;|&nbsp;&nbsp; 0400 555 123
  </div>
</section>

<footer>
  <div class="footer"></div>
  <div class="partner" style="top:4183px">SunField</div>
  <div class="partner" style="top:4256px">HeatBright</div>
  <div class="partner" style="top:4325px">Citrus Pumps</div>

  <h4 class="foot-title" style="left:344px">Quick Link</h4>
  <ul class="foot-links">
    <li>Home</li><li>About Us</li><li>Services</li><li>Septic</li><li>Products</li><li>Showroom</li><li>Contact Us</li>
  </ul>

  <h4 class="foot-title" style="left:505px">Let Me Fix Your Taps</h4>
  <div class="foot-info" style="top:4222px;align-items:flex-start;line-height:24px">
    <svg width="12" height="14" viewBox="0 0 24 28" style="margin-top:5px"><path d="M12 1a9 9 0 0 0-9 9c0 7 9 17 9 17s9-10 9-17a9 9 0 0 0-9-9z" fill="none" stroke="#fff" stroke-width="2.5"/><circle cx="12" cy="10" r="3" fill="#fff"/></svg>
    <span>27 Harlow Street, Brenmoor<br>WA 6999</span>
  </div>
  <div class="foot-info" style="top:4295px"><svg width="14" height="12" viewBox="0 0 24 20"><rect x="2" y="6" width="20" height="12" rx="2" fill="none" stroke="#fff" stroke-width="2"/><path d="M4 6c2-4 14-4 16 0" fill="none" stroke="#fff" stroke-width="2"/></svg>1800 000 321</div>
  <div class="foot-info" style="top:4319px"><svg width="14" height="12" viewBox="0 0 24 20"><rect x="2" y="6" width="20" height="12" rx="2" fill="none" stroke="#fff" stroke-width="2"/><path d="M4 6c2-4 14-4 16 0" fill="none" stroke="#fff" stroke-width="2"/></svg>0400 555 123</div>
  <div class="foot-info" style="top:4343px"><svg width="14" height="12" viewBox="0 0 24 20"><rect x="2" y="4" width="20" height="14" rx="2" fill="none" stroke="#fff" stroke-width="2"/><path d="M6 4v-2h12v2" fill="none" stroke="#fff" stroke-width="2"/></svg>PO Box 88 Brenmoor WA 6999</div>
  <div class="foot-info" style="top:4367px"><svg width="14" height="12" viewBox="0 0 24 20"><rect x="2" y="3" width="20" height="14" rx="1" fill="none" stroke="#fff" stroke-width="2"/><path d="M2 4l10 7 10-7" fill="none" stroke="#fff" stroke-width="2"/></svg>office@letmefixyourtaps.com.au</div>
  <div class="pay" style="left:505px">Online</div>
  <div class="pay" style="left:547px">Debit</div>
  <div class="pay" style="left:589px">Credit</div>
  <div class="pay" style="left:631px">Card</div>

  <div class="about-card">
    <div class="brand" style="font-size:15px"><span class="dot"></span>LET ME FIX YOUR TAPS</div>
    <p style="font-size:11.5px;line-height:15px;color:var(--muted);margin-top:22px">Let Me Fix Your Taps is a family run business based in Brenmoor since 2004, we service Ashvale to Kellow, Fernridge to Dunmore....</p>
    <h4 style="font-size:14px;margin-top:24px">We Give Pensioner Discounts</h4>
    <div style="display:flex;gap:18px;margin-top:20px;align-items:center">
      <span style="width:44px;height:64px;border:3px solid var(--navy);border-radius:22px 22px 4px 4px;background:#dfe7f4"></span>
      <span style="width:64px;height:64px;border:4px solid var(--navy);border-radius:50%;background:#dfe7f4"></span>
      <span style="width:58px;height:58px;border:4px solid #3d9b3d;border-radius:50%;background:#e6f3e0"></span>
    </div>
  </div>

  <p class="copyright">© 2020 <b style="color:var(--navy);font-weight:600">Let Me Fix Your Taps</b>. All Rights Reserved.</p>
  <span class="social" style="left:1000px;background:var(--blue)" aria-label="Social link"></span>
  <span class="social" style="left:1037px;background:var(--navy)" aria-label="Social link"></span>
  <span class="social" style="left:1074px;background:var(--navy)" aria-label="Social link"></span>
  <span class="social" style="left:1111px;background:var(--navy)" aria-label="Social link"></span>
</footer>

</body>
</html>
```